Need Business Cards, Letterhead, and Stationary

Hi, please design a full stationary set for the attached logo (Business Cards, Letterhead, A4 Envelope, and other important stationary items that you can think of)
Please be as creative as you wish. The logo is for An Entrepreneurship Academy that teaches young and starting Entrepreneur skills they need to start their business.

```html
<!DOCTYPE html>
<html lang="en">
<head>
<meta charset="utf-8">
<title>Sprout Stationery Set</title>
<link rel="stylesheet" href="https://fonts.googleapis.com/css2?family=Josefin+Slab:wght@400;600&family=Open+Sans:wght@400;700&display=swap">
<style>
  :root {
    --backdrop: #d8d8d8;
    --paper: #ffffff;
    --charcoal: #3a3a3a;
    --ink-black: #1c1c1c;
    --body-ink: #4a4a4a;
    --muted: #9a9a9a;
    --sun: #f2b705;
    --sky: #2b78c2;
  }
  html, body { margin: 0; padding: 0; }
  body {
    width: 1200px; height: 642px; overflow: hidden; position: relative;
    background: var(--backdrop);
    font-family: "Open Sans", Arial, sans-serif;
  }
  .item { position: absolute; box-sizing: border-box; }

  /* Wordmark stand-in */
  .wordmark { display: flex; align-items: center; gap: 5px; color: var(--paper); font-weight: 700; letter-spacing: .5px; }
  .wordmark .dot { border-radius: 50%; background: var(--sun); flex: none; }
  .tagline { color: var(--muted); font-size: 3px; letter-spacing: .4px; text-transform: uppercase; }

  /* Letterhead */
  .letterhead { left: 181px; top: 42px; width: 346px; height: 521px; background: var(--paper); }
  .letterhead .header-block {
    position: absolute; left: 118px; top: 29px; width: 110px; height: 47px; background: var(--charcoal);
    display: flex; flex-direction: column; align-items: center; justify-content: center; gap: 2px;
  }
  .letterhead .header-block .wordmark { font-size: 13px; }
  .letterhead .header-block .dot { width: 9px; height: 9px; }
  .letterhead .letter-body {
    position: absolute; left: 48px; top: 177px; width: 253px;
    font-family: "Josefin Slab", Georgia, serif; font-size: 6.6px; line-height: 8.3px; color: var(--body-ink);
    text-align: justify;
  }
  .letterhead .letter-body p { margin: 0 0 9px; }
  .letterhead .letter-contact {
    position: absolute; left: 0; right: 0; top: 458px; text-align: center;
    font-family: "Josefin Slab", Georgia, serif; font-size: 6.4px; line-height: 10px; color: var(--body-ink);
  }
  .letterhead .letter-contact .phone { margin-bottom: 11px; }
  .letterhead .footer-strip {
    position: absolute; left: 117px; bottom: 0; width: 111px; height: 15px; background: var(--charcoal);
    color: #cfcfcf; font-size: 4.6px; display: flex; align-items: center; justify-content: center;
  }

  /* Business card front */
  .card-front { left: 587px; top: 70px; width: 130px; height: 87px; background: var(--paper); }
  .card-front .wordmark { position: absolute; left: 6px; top: 12px; color: var(--charcoal); font-size: 8px; gap: 2px; }
  .card-front .wordmark .dot { width: 5px; height: 5px; }
  .card-front .divider { position: absolute; left: 52px; top: 9px; width: 1px; height: 70px; background: #bdbdbd; }
  .card-front .details { position: absolute; left: 57px; top: 8px; color: var(--charcoal); }
  .card-front .name { font-size: 10px; line-height: 12px; font-weight: 400; }
  .card-front .name b { font-weight: 700; }
  .card-front .role { font-size: 4.4px; font-weight: 700; margin-bottom: 7px; }
  .card-front .fine { font-size: 3.6px; line-height: 4.6px; }
  .card-front .fine + .fine { margin-top: 5px; }

  /* Business card back */
  .card-back {
    left: 589px; top: 188px; width: 123px; height: 89px; background: var(--charcoal);
  }
  .card-back .wordmark { position: absolute; left: 0; right: 0; top: 30px; justify-content: center; font-size: 13px; }
  .card-back .wordmark .dot { width: 9px; height: 9px; }
  .card-back .web { position: absolute; left: 0; right: 0; bottom: 7px; text-align: center; color: #d6d6d6; font-size: 4.2px; }

  /* Notebook cover */
  .notebook { left: 590px; top: 325px; width: 167px; height: 245px; background: var(--ink-black); }
  .notebook .wordmark { position: absolute; right: 8px; bottom: 16px; font-size: 10px; gap: 3px; }
  .notebook .wordmark .dot { width: 7px; height: 7px; }

  /* Envelope */
  .envelope { left: 800px; top: 27px; width: 358px; height: 581px; background: var(--paper); }
  .envelope .flap { position: absolute; left: 0; top: 0; width: 358px; height: 60px; }
  .envelope .brand-band {
    position: absolute; left: 10px; top: 48px; width: 83px; height: 478px; background: var(--charcoal);
  }
  .envelope .brand-band .wordmark { position: absolute; left: 0; right: 0; top: 62px; justify-content: center; font-size: 14px; }
  .envelope .brand-band .wordmark .dot { width: 9px; height: 9px; }
  .envelope .brand-band .tagline { position: absolute; left: 0; right: 0; top: 84px; text-align: center; }
  .envelope .brand-band .address {
    position: absolute; left: 4px; bottom: 6px; color: #a8a8a8; font-size: 3.6px; line-height: 4.7px;
  }
  .envelope .brand-band .address p { margin: 0 0 5px; }
  .envelope .side-web {
    position: absolute; left: 96px; top: 22px; color: #cfcfcf; font-size: 8px; letter-spacing: .3px;
    writing-mode: vertical-rl;
  }
  .envelope .window {
    position: absolute; left: 194px; top: 448px; width: 131px; height: 71px;
    background: #f0f0f0; border: 1px solid #e0e0e0;
  }
</style>
</head>
<body>

  <!-- Letterhead -->
  <section class="item letterhead">
    <div class="header-block">
      <div class="wordmark"><span class="dot"></span>SPROUT</div>
      <div class="tagline">Founders Learning Academy</div>
    </div>
    <div class="letter-body">
      <p>Lorem ipsum dolor sit amet,</p>
      <p>Lorem ipsum dolor sit amet, consectetur adipiscing elit. Donec orci purus, luctus vitae dignissim eu, iaculis sed purus. Vivamus faucibus, ipsum nec aliquet viverra, leo mauris condimentum ligula, sit amet sagittis enim ligula quis arcu. Nam egestas tortor id nisi porttitor mattis. In tortor ante, ultricies in suscipit a, tempus non massa. Vivamus et auctor mi. Fusce vel massa nulla. Phasellus nec eros mauris, et scelerisque orci. Donec malesuada orci vitae nulla accumsan porta a id massa. Quisque accumsan iaculis magna et amet fringilla. Maecenas consequat, magna eget tincidunt semper, odio nibh rutrum mi, id feugiat ante nisi eu risus. Vestibulum nunc orci, rhoncus a placerat in, ultricies in mi. Cras mattis varius eros, vel fringilla nisi suscipit eget.</p>
      <p>Quisque scelerisque sagittis nulla at porttitor. Mauris a justo et tellus interdum tristique. Sed id augue vitae urna euismod commodo aliquet a quam. Pellentesque arcu velit, cursus et malesuada ut, consequat et diam. Nullam erat sem, rhoncus id ullamcorper vitae, rhoncus et arcu. In ultricies ultricies nulla, ut rutrum nisi iaculis at. Donec eu magna a metus ornare faucibus. Fusce aliquet faucibus ultricies. Morbi semper, est id tincidunt gravida, sem arcu adipiscing lacus, ac bibendum nulla leo eu purus. Quisque nec diam sed risus consectetur a cursus quis quis nibh. Vestibulum id purus lorem.</p>
      <p>Vivamus vehicula accumsan lacinia. Aliquam erat volutpat. Pellentesque consequat venenatis velit non gravida. Etiam et sem et nulla congue aliquam sed eget augue. Nulla facilisi. Pellentesque habitant morbi tristique senectus et netus et malesuada fames ac turpis egestas. Nulla a elit at sem iaculis congue. Nullam mollis tristique lobortis.</p>
    </div>
    <div class="letter-contact">
      <div class="phone">(992) 555-1234</div>
      <div>yourname@yourwebsite.com</div>
      <div>yourwebsite.com</div>
    </div>
    <div class="footer-strip">www.sproutfounders.com</div>
  </section>

  <!-- Business card, front -->
  <section class="item card-front">
    <div class="wordmark"><span class="dot"></span>SPROUT</div>
    <div class="divider"></div>
    <div class="details">
      <div class="name">Karim <b>Nadeem</b></div>
      <div class="role">C.E.O.</div>
      <div class="fine">Marina Crest Tower<br>Level 12, P.O. Box 4410<br>Dubai<br>United Arab Emirates</div>
      <div class="fine">Office: +971 4 555 0142<br>Fax: +971 4 555 0199<br>Email: karim@sproutfounders.com</div>
    </div>
  </section>

  <!-- Business card, back -->
  <section class="item card-back">
    <div class="wordmark"><span class="dot"></span>SPROUT</div>
    <div class="web">www.sproutfounders.com</div>
  </section>

  <!-- Notebook cover -->
  <section class="item notebook">
    <div class="wordmark"><span class="dot"></span>SPROUT</div>
  </section>

  <!-- Envelope -->
  <section class="item envelope">
    <svg class="flap" viewBox="0 0 358 60" aria-hidden="true">
      <polyline points="0,0 179,46 358,0" fill="none" stroke="#ececec" stroke-width="1"/>
    </svg>
    <div class="brand-band">
      <div class="wordmark"><span class="dot"></span>SPROUT</div>
      <div class="tagline">Founders Learning Academy</div>
      <div class="address">
        <p>Marina Crest Tower<br>Level 12, P.O. Box 4410<br>Dubai<br>United Arab Emirates</p>
        <p>Office: +971 4 555 0142<br>Fax: +971 4 555 0199<br>Email: karim@sproutfounders.com</p>
      </div>
    </div>
    <div class="side-web">www.sproutfounders.com</div>
    <div class="window"></div>
  </section>

</body>
</html>
```